Upscale business cards needed for Board of Directors

We need professional business cards created for members of our family business Board of Directors. We would like these relatively simple and straightforward, but also with a unique element to set them apart. Probably stick with neutral and simple colors - white, grey etc. We need space for the traditional elements, including name, title, address, email/phone number. And we will be creating several from this template so it needs to be template that is easy to switch information in and out of.
Business
See description

```html
<!DOCTYPE html>
<html lang="en">
<head>
<meta charset="utf-8">
<title>Braemoor Holdings – Business Card</title>
<link rel="stylesheet" href="https://fonts.googleapis.com/css2?family=Open+Sans:wght@400;700&family=Raleway:wght@300;400&display=swap">
<style>
  :root {
    --page-bg: #ffffff;
    --card-dark: #2b2a29;
    --accent-gold: #b9a57a;
    --text-light: #ffffff;
    --text-soft: #e6e4e0;
  }
  * { margin: 0; padding: 0; box-sizing: border-box; }
  html, body {
    width: 1200px;
    height: 832px;
    overflow: hidden;
    background: var(--page-bg);
  }
  .canvas {
    position: relative;
    width: 1200px;
    height: 832px;
  }
  .business-card {
    position: absolute;
    left: 177px;
    top: 161px;
    width: 810px;
    height: 451px;
    background: var(--card-dark);
    overflow: hidden;
  }
  .top-band {
    position: absolute;
    left: 0; top: 0;
    width: 100%;
    height: 64px;
    background: var(--accent-gold);
  }
  .accent-rule {
    position: absolute;
    left: 0; top: 70px;
    width: 805px;
    height: 5px;
    background: var(--accent-gold);
  }
  .company-name {
    position: absolute;
    left: 0; top: 88px;
    width: 100%;
    text-align: center;
    font-family: "Open Sans", sans-serif;
    font-weight: 700;
    color: var(--text-light);
    line-height: 1;
  }
  .company-name .primary {
    display: block;
    font-size: 43px;
    letter-spacing: 1px;
  }
  .company-name .secondary {
    display: block;
    margin-top: 8px;
    font-size: 21px;
    letter-spacing: 7px;
    padding-left: 7px;
  }
  .person {
    position: absolute;
    right: 469px;
    top: 252px;
    text-align: right;
    color: var(--text-light);
  }
  .person-name {
    font-family: "Open Sans", sans-serif;
    font-weight: 700;
    font-size: 23px;
    line-height: 1.3;
  }
  .person-title {
    font-family: "Raleway", sans-serif;
    font-weight: 400;
    font-size: 21px;
    color: var(--text-soft);
    line-height: 1.4;
  }
  .divider {
    position: absolute;
    left: 372px;
    top: 205px;
    width: 3px;
    height: 184px;
    background: var(--accent-gold);
  }
  .contact-list {
    position: absolute;
    left: 400px;
    top: 203px;
    list-style: none;
  }
  .contact-item {
    display: flex;
    align-items: center;
    height: 40px;
    font-family: "Raleway", sans-serif;
    font-weight: 400;
    font-size: 23px;
    color: var(--text-light);
  }
  .contact-icon {
    width: 20px;
    height: 22px;
    margin-right: 8px;
    flex: none;
  }
  .contact-icon path,
  .contact-icon rect,
  .contact-icon circle,
  .contact-icon line {
    fill: none;
    stroke: var(--accent-gold);
    stroke-width: 1.6;
  }
  .contact-icon .solid { fill: var(--accent-gold); stroke: none; }
</style>
</head>
<body>
<main class="canvas">
  <section class="business-card" aria-label="Business card">
    <div class="top-band"></div>
    <div class="accent-rule"></div>

    <h1 class="company-name">
      <span class="primary">BRAEMOOR</span>
      <span class="secondary">HOLDINGS</span>
    </h1>

    <div class="person">
      <p class="person-name">NAME SURNAME</p>
      <p class="person-title">Position</p>
    </div>

    <div class="divider"></div>

    <ul class="contact-list">
      <li class="contact-item">
        <svg class="contact-icon" viewBox="0 0 20 22" aria-hidden="true">
          <path d="M5 3 L8 3 L9 7 L7 9 Q9 14 13 16 L15 14 L18 15 L18 18 Q16 20 13 19 Q5 15 3 7 Q3 4 5 3 Z"/>
        </svg>
        012 345 67890
      </li>
      <li class="contact-item">
        <svg class="contact-icon" viewBox="0 0 20 22" aria-hidden="true">
          <rect x="5" y="3" width="11" height="17" rx="1.5"/>
          <line x1="9" y1="17" x2="12" y2="17"/>
        </svg>
        012 345 67891
      </li>
      <li class="contact-item">
        <svg class="contact-icon" viewBox="0 0 20 22" aria-hidden="true">
          <rect x="2" y="8" width="16" height="10"/>
          <path d="M2 8 L10 14 L18 8"/>
        </svg>
        info@company.com
      </li>
      <li class="contact-item">
        <svg class="contact-icon" viewBox="0 0 20 22" aria-hidden="true">
          <circle cx="10" cy="12" r="7"/>
          <path d="M3 12 H17 M10 5 Q6 12 10 19 M10 5 Q14 12 10 19"/>
        </svg>
        www.company.com
      </li>
      <li class="contact-item">
        <svg class="contact-icon" viewBox="0 0 20 22" aria-hidden="true">
          <path class="solid" d="M10 1 Q16 1 16 8 Q16 12 10 20 Q4 12 4 8 Q4 1 10 1 Z M10 5 A3 3 0 1 0 10.01 5 Z" fill-rule="evenodd"/>
        </svg>
        Address
      </li>
    </ul>
  </section>
</main>
</body>
</html>
```